Assisted living facility needs a business card design

We need a business card design for an assisted living facility in Los Angeles. We have a logo selected but we would like a business card design that will leave a lasting impression on families looking to place their elderly loved ones in our care as well as on other facility providers who may refer their elderly residents to our facility.

```html
<!DOCTYPE html>
<html lang="en">
<head>
<meta charset="utf-8">
<title>Havenbrook Crest Senior Living – Business Card</title>
<link href="https://fonts.googleapis.com/css2?family=Poppins:wght@400;500;600&display=swap" rel="stylesheet">
<style>
  :root {
    --stage: #454545;
    --brand-blue: #0079CE;
    --brand-blue-soft: #2A8FD8;
    --paper: #ffffff;
    --divider-grey: #808080;
  }
  * { margin: 0; padding: 0; box-sizing: border-box; }
  html, body { width: 1200px; height: 1200px; overflow: hidden; }
  body {
    background: var(--stage);
    font-family: "Poppins", sans-serif;
    position: relative;
  }
  .card {
    position: absolute;
    top: 303px;
    width: 366px;
    height: 594px;
    overflow: hidden;
    box-shadow: 3px 3px 4px rgba(0,0,0,0.55);
  }
  .card--front { left: 201px; background: var(--brand-blue); }
  .card--back { left: 599px; background: var(--paper); }

  .front-backdrop {
    position: absolute; inset: 0;
    background:
      radial-gradient(ellipse 70% 55% at 30% 25%, var(--brand-blue-soft) 0%, rgba(42,143,216,0) 70%),
      radial-gradient(ellipse 65% 50% at 75% 70%, var(--brand-blue-soft) 0%, rgba(42,143,216,0) 70%),
      var(--brand-blue);
  }

  .brand-name {
    position: absolute;
    left: 0; right: 0;
    text-align: center;
    font-family: "Poppins", sans-serif;
    font-weight: 500;
    letter-spacing: 2px;
    line-height: 1.25;
  }
  .brand-name__main { display: block; font-size: 25px; }
  .brand-name__sub { display: block; font-size: 12px; letter-spacing: 5px; margin-top: 14px; }
  .card--front .brand-name { top: 485px; color: var(--paper); }
  .card--back .brand-name { top: 141px; color: var(--brand-blue); }

  .back-divider {
    position: absolute; left: 0; right: 0; top: 286px;
    height: 4px; background: var(--divider-grey);
  }
  .back-panel {
    position: absolute; left: 0; right: 0; top: 293px; bottom: 0;
    background: var(--brand-blue);
    color: var(--paper);
    text-align: center;
  }
  .person-name {
    position: absolute; left: 0; right: 0; top: 42px;
    font-size: 26px; font-weight: 600; line-height: 1.2;
  }
  .person-role {
    position: absolute; left: 0; right: 0; top: 70px;
    font-size: 16.5px; font-weight: 400;
  }
  .icon-row {
    position: absolute; left: 0; right: 0; top: 102px;
    display: flex; justify-content: center; align-items: center; gap: 4px;
  }
  .icon-row__rule { width: 52px; height: 1px; background: var(--paper); opacity: 0.8; margin: 0 4px; }
  .icon-tile {
    width: 25px; height: 25px; background: var(--paper); border-radius: 3px;
    display: flex; align-items: center; justify-content: center;
  }
  .contact-list {
    position: absolute; left: 0; right: 0; top: 135px;
    list-style: none; font-size: 16.5px; line-height: 21px;
  }
  .panel-rule {
    position: absolute; left: 88px; right: 88px; top: 214px;
    height: 1px; background: var(--paper); opacity: 0.8;
  }
  .address {
    position: absolute; left: 0; right: 0; top: 228px;
    font-style: normal; font-size: 16.5px; line-height: 21px;
  }
</style>
</head>
<body>
  <section class="card card--front" aria-label="Card front">
    <div class="front-backdrop" role="img" aria-label="Faint repeated brand-name pattern backdrop in soft blue tones"></div>
    <div class="brand-name">
      <span class="brand-name__main">HAVENBROOK CREST</span>
      <span class="brand-name__sub">SENIOR LIVING</span>
    </div>
  </section>

  <section class="card card--back" aria-label="Card back">
    <div class="brand-name">
      <span class="brand-name__main">HAVENBROOK CREST</span>
      <span class="brand-name__sub">SENIOR LIVING</span>
    </div>
    <div class="back-divider"></div>
    <div class="back-panel">
      <h1 class="person-name">Daniel Harper</h1>
      <p class="person-role">Managing Director</p>
      <div class="icon-row">
        <span class="icon-row__rule"></span>
        <span class="icon-tile" aria-label="Phone">
          <svg width="17" height="17" viewBox="0 0 24 24" fill="var(--brand-blue)"><path d="M2 9c0-2 4-4 10-4s10 2 10 4v2h-5V9.5C15 9 13.5 9 12 9s-3 0-5 .5V11H2z"/><path d="M6 12h12l2 8H4z"/><circle cx="12" cy="16" r="2" fill="#fff"/></svg>
        </span>
        <span class="icon-tile" aria-label="Email">
          <svg width="17" height="17" viewBox="0 0 24 24" fill="none" stroke="var(--brand-blue)" stroke-width="2"><rect x="3" y="6" width="18" height="12"/><path d="M3 6l9 7 9-7M3 18l7-6M21 18l-7-6"/></svg>
        </span>
        <span class="icon-tile" aria-label="Website">
          <svg width="17" height="17" viewBox="0 0 24 24" fill="none" stroke="var(--brand-blue)" stroke-width="2"><circle cx="12" cy="12" r="9"/><path d="M3 12h18M12 3c3 3 3 15 0 18M12 3c-3 3-3 15 0 18"/></svg>
        </span>
        <span class="icon-row__rule"></span>
      </div>
      <ul class="contact-list">
        <li>044-555 210 318</li>
        <li>info@havenbrookcrest.com</li>
        <li>www.havenbrookcrest.com</li>
      </ul>
      <div class="panel-rule"></div>
      <address class="address">218 Maple Grove Avenue<br>90024, Los Angeles</address>
    </div>
  </section>
</body>
</html>
```